Halvern Assay Advisors.

Cellular Assay Advisory Services. Planning, Testing and Verification of Tissue Stain and Imaging Methods.

Industry/Entity Type

Consulting

Contact Information for Business Card

Halvern Assay Advisors
Cell: 614 905-7738
Dale Morrow
dmorrow4817@quillpost.net

```html
<!DOCTYPE html>
<html lang="en">
<head>
<meta charset="utf-8">
<title>Halvern Assay Advisors – Business Card</title>
<link rel="stylesheet" href="https://fonts.googleapis.com/css2?family=Ubuntu:wght@400;500;700&family=Arimo:ital,wght@0,700;1,700&display=swap">
<style>
  :root {
    --page-bg: #efefef;
    --panel-teal: rgba(33, 91, 115, 0.96);
    --panel-text: #b9c6cf;
    --name-text: #cfcfcf;
    --icon-disc: #8ea6b6;
    --icon-glyph: #2a5d76;
    --caption-band: rgba(28, 52, 66, 0.88);
    --caption-text: #cdd6db;
    --micro-dark: #0d1a12;
    --micro-green: #2f7a3c;
    --dna-deep: #0f3f63;
    --dna-bright: #4fb8e0;
  }
  * { box-sizing: border-box; margin: 0; padding: 0; }
  html, body {
    width: 1200px; height: 1000px; overflow: hidden;
    background: var(--page-bg);
  }
  .canvas { position: relative; width: 1200px; height: 1000px; }

  .card { position: absolute; overflow: hidden; }

  /* Front card */
  .card--front { left: 305px; top: 27px; width: 838px; height: 455px; }
  .front-photo {
    position: absolute; inset: 0;
    background:
      radial-gradient(ellipse at 30% 45%, rgba(60, 140, 70, 0.55), transparent 55%),
      radial-gradient(ellipse at 90% 80%, rgba(70, 170, 80, 0.5), transparent 45%),
      linear-gradient(160deg, #0a1510, var(--micro-green) 45%, var(--micro-dark));
  }
  .company-band {
    position: absolute; left: 28px; top: 0; width: 779px; height: 110px;
    background: var(--panel-teal); border-radius: 0 0 12px 12px;
    display: flex; align-items: center; justify-content: center;
  }
  .company-name {
    font-family: "Ubuntu", sans-serif; font-weight: 700; font-size: 38px;
    letter-spacing: 2.4px; color: var(--panel-text);
  }
  .person-name {
    position: absolute; left: 0; right: 0; top: 128px; text-align: center;
    font-family: "Arimo", sans-serif; font-style: italic; font-weight: 700;
    font-size: 72px; letter-spacing: 3px; color: var(--name-text);
    padding-left: 40px;
  }
  .contact-panel {
    position: absolute; left: 28px; top: 225px; width: 779px; height: 240px;
    background: var(--panel-teal); border-radius: 12px 12px 0 0;
  }
  .contact-icon { position: absolute; left: 361px; width: 58px; height: 58px; }
  .contact-icon--phone { top: 12px; }
  .contact-icon--mail { top: 119px; }
  .contact-line {
    position: absolute; left: 0; right: 0; text-align: center;
    font-family: "Arimo", sans-serif; font-weight: 700; font-size: 30px;
    letter-spacing: 1.5px; color: var(--panel-text);
  }
  .contact-line--phone { top: 76px; }
  .contact-line--mail { top: 183px; font-size: 29px; }

  /* Back card */
  .card--back { left: 53px; top: 512px; width: 840px; height: 455px; }
  .back-illustration {
    position: absolute; inset: 0;
    background:
      radial-gradient(ellipse at 35% 40%, rgba(79, 184, 224, 0.7), transparent 50%),
      radial-gradient(ellipse at 80% 30%, rgba(79, 184, 224, 0.35), transparent 40%),
      linear-gradient(135deg, #1b6a9a, var(--dna-deep) 60%, #22617e);
  }
  .caption-band {
    position: absolute; left: 0; right: 0; bottom: 0; height: 150px;
    background: var(--caption-band);
    display: flex; align-items: center; justify-content: center;
    padding-right: 20px;
  }
  .caption-text {
    font-family: "Ubuntu", sans-serif; font-weight: 500; font-size: 34px;
    line-height: 43px; letter-spacing: 2px; text-align: center;
    color: var(--caption-text);
  }
</style>
</head>
<body>
<main class="canvas">

  <section class="card card--front">
    <div class="front-photo" role="img" aria-label="Dark fluorescence microscopy image with green stained tissue"></div>
    <header class="company-band">
      <h1 class="company-name">Halvern Assay Advisors</h1>
    </header>
    <p class="person-name">Dale Morrow</p>
    <div class="contact-panel">
      <svg class="contact-icon contact-icon--phone" viewBox="0 0 58 58" aria-hidden="true">
        <circle cx="29" cy="29" r="29" fill="var(--icon-disc)"/>
        <path d="M21 16c1.5-1 3-.6 3.8.8l2.6 4.6c.7 1.3.3 2.6-.8 3.4l-1.8 1.3c1.2 3 3.6 5.6 6.6 7l1.4-1.8c.8-1.1 2.2-1.4 3.4-.7l4.5 2.7c1.3.8 1.6 2.4.7 3.8l-1.5 2.2c-1.2 1.6-3.2 2.2-5 1.6C26.5 38.4 19.6 31.4 17.2 22.8c-.5-1.8.1-3.8 1.7-4.9z" fill="var(--icon-glyph)"/>
      </svg>
      <p class="contact-line contact-line--phone">614 905-7738</p>
      <svg class="contact-icon contact-icon--mail" viewBox="0 0 58 58" aria-hidden="true">
        <circle cx="29" cy="29" r="29" fill="var(--icon-disc)"/>
        <rect x="15" y="19" width="28" height="20" fill="none" stroke="var(--icon-glyph)" stroke-width="2.4"/>
        <path d="M15 19l14 11 14-11M15 39l10-9M43 39l-10-9" fill="none" stroke="var(--icon-glyph)" stroke-width="2.4"/>
      </svg>
      <p class="contact-line contact-line--mail">dmorrow4817@quillpost.net</p>
    </div>
  </section>

  <section class="card card--back">
    <div class="back-illustration" role="img" aria-label="Glowing blue 3D DNA double helix illustration"></div>
    <div class="caption-band">
      <p class="caption-text">Cellular Assay Advisory Services.<br>Planning, Testing and Verification<br>of Tissue Stain and Imaging Methods.</p>
    </div>
  </section>

</main>
</body>
</html>
```